I need a business card to reflect my new qualifications.
Accredited Teacher, Accredited Valuer & Accredited Judge of Patchwork Quilting.
Fennick Lane Studio
47 Marlow Road, Wodonga Vic 3690
0412 378 906 fennick@brelnet.com.au

```html
<!DOCTYPE html>
<html lang="en">
<head>
<meta charset="utf-8">
<title>Fennick Lane Studio – Business Card</title>
<link rel="stylesheet" href="https://fonts.googleapis.com/css2?family=Dancing+Script:wght@400&family=Josefin+Sans:wght@300&display=swap">
<style>
  :root {
    --card-bg: #d8f4f3;
    --plaid-line: rgba(120, 165, 170, 0.32);
    --plaid-faint: rgba(120, 165, 170, 0.16);
    --ink: #7a2a12;
    --emblem: #77604d;
    --emblem-shadow: rgba(110, 80, 60, 0.28);
  }
  * { margin: 0; padding: 0; box-sizing: border-box; }
  html, body {
    width: 1200px;
    height: 823px;
    overflow: hidden;
    background: var(--card-bg);
  }
  .card {
    position: relative;
    width: 1200px;
    height: 823px;
    background: var(--card-bg);
    overflow: hidden;
  }
  .card__plaid {
    position: absolute;
    inset: 0;
    width: 100%;
    height: 100%;
  }
  .card__name {
    position: absolute;
    top: 172px;
    left: 0;
    width: 100%;
    text-align: center;
    font-family: "Dancing Script", cursive;
    font-weight: 400;
    font-size: 114px;
    line-height: 1;
    color: var(--ink);
    letter-spacing: 1px;
  }
  .card__credentials {
    position: absolute;
    top: 318px;
    left: 0;
    width: 100%;
    text-align: center;
    font-family: "Josefin Sans", sans-serif;
    font-weight: 300;
    font-size: 21px;
    line-height: 28px;
    letter-spacing: 2px;
    color: var(--ink);
    text-transform: uppercase;
    white-space: nowrap;
  }
  .card__emblem {
    position: absolute;
    left: 500px;
    top: 377px;
    width: 198px;
    height: 197px;
    background: var(--emblem);
  }
  .card__emblem-shadow {
    position: absolute;
    left: 450px;
    top: 562px;
    width: 300px;
    height: 26px;
    border-radius: 50%;
    background: radial-gradient(ellipse at center, var(--emblem-shadow) 0%, rgba(110, 80, 60, 0) 70%);
  }
  .card__contact {
    position: absolute;
    top: 683px;
    left: 0;
    width: 100%;
    text-align: center;
    font-family: "Josefin Sans", sans-serif;
    font-weight: 300;
    font-size: 45px;
    line-height: 60px;
    color: var(--ink);
    text-transform: uppercase;
  }
  .card__contact-line { display: block; white-space: nowrap; }
  .card__contact-line--second { font-size: 42px; }
  .card__phone { margin-right: 26px; }
</style>
</head>
<body>
<div class="card">
  <svg class="card__plaid" viewBox="0 0 1200 823" aria-hidden="true">
    <g stroke="var(--plaid-faint)" stroke-width="2">
      <line x1="0" y1="46" x2="1200" y2="46"/>
      <line x1="0" y1="74" x2="1200" y2="74"/>
      <line x1="0" y1="108" x2="1200" y2="108"/>
    </g>
    <g stroke="var(--plaid-line)" stroke-width="2.5" stroke-dasharray="70 14">
      <line x1="52" y1="0" x2="52" y2="823"/>
      <line x1="66" y1="0" x2="66" y2="823"/>
      <line x1="80" y1="0" x2="80" y2="823"/>
      <line x1="114" y1="0" x2="114" y2="823"/>
      <line x1="1086" y1="0" x2="1086" y2="823"/>
      <line x1="1120" y1="0" x2="1120" y2="823"/>
      <line x1="1134" y1="0" x2="1134" y2="823"/>
      <line x1="1149" y1="0" x2="1149" y2="823"/>
    </g>
  </svg>

  <h1 class="card__name">Fennick Lane Studio</h1>

  <p class="card__credentials">Accredited Teacher · Valuer · Judge of Patchwork Quilting</p>

  <div class="card__emblem-shadow" aria-hidden="true"></div>
  <div class="card__emblem" role="img" aria-label="Studio emblem: square tile with a pale interlaced leaf and vine ornament"></div>

  <p class="card__contact">
    <span class="card__contact-line">47 Marlow Road, Wodonga Vic 3690</span>
    <span class="card__contact-line card__contact-line--second"><span class="card__phone">0412 378 906</span>fennick@brelnet.com.au</span>
  </p>
</div>
</body>
</html>
```